Postcard Design Harlow Bend D to D

Residential Real Estate, we want to implement a mail campaign in an specific geographic area.We want to include Market information on the area and statistics of the real estate market.This piece is going to be deliver via mail service door to door.

Target Market(s)

Home owners that might be interested in selling their houses

Industry/Entity Type

Real Estate

Font styles to use
Sans Serif

Colors
ec1f27
f78f20

Requirements
Must have
• Attractive look
• Include the information that we just sent to you
• Clear graphics and tables
• Must include clear information about our group

```html
<!DOCTYPE html>
<html lang="en">
<head>
<meta charset="utf-8">
<title>Harlow Bend Market Report Postcard</title>
<link href="https://fonts.googleapis.com/css2?family=Mulish:ital,wght@0,400;0,600;0,700;0,800;1,400;1,600;1,700;1,800&display=swap" rel="stylesheet">
<style>
  :root{
    --stage:#6b6b6b;
    --paper:#fbf9f3;
    --white:#ffffff;
    --brand-red:#a3202b;
    --accent-orange:#f0821f;
    --ink:#3a3a3a;
    --ink-soft:#5b5b5b;
    --rule:#8a8a8a;
    --map-bg:#eef0ec;
    --photo-sky:#b9c9cf;
    --photo-lawn:#7e9a52;
  }
  *{box-sizing:border-box;margin:0;padding:0}
  html,body{width:1200px;height:825px;overflow:hidden}
  body{background:var(--stage);font-family:"Mulish",Arial,sans-serif;color:var(--ink);position:relative}
  .postcard{position:absolute;left:60px;top:65px;width:1080px;height:695px;background:var(--paper);overflow:hidden}
  .postcard *{position:absolute}

  .area-map{right:0;top:0;width:300px;height:200px;background:linear-gradient(160deg,var(--map-bg),#e3e6df)}

  .title{left:40px;top:26px;font-size:63px;line-height:1.1;font-weight:800;font-style:italic;color:var(--brand-red);letter-spacing:-1.2px;white-space:nowrap}
  .subtitle{left:448px;top:38px;font-size:23px;line-height:28px;font-weight:700;font-style:italic;color:var(--ink-soft);white-space:nowrap}
  .title-rule{left:40px;top:115px;width:585px;height:1px;background:var(--rule)}
  .report-date{left:638px;top:104px;font-size:15px;font-weight:700;font-style:italic;color:var(--brand-red);white-space:nowrap}

  .greeting{left:42px;top:139px;font-size:14px;font-weight:800;font-style:italic;color:var(--ink)}
  .intro{left:42px;top:161px;width:520px;font-size:15px;line-height:19px;font-style:italic;color:var(--ink)}
  .intro p{position:static;margin-bottom:7px}

  .facts{left:36px;top:273px;width:263px;height:148px;border:1px solid var(--rule);background:var(--white)}
  .facts-head{left:6px;top:6px;width:249px;height:28px;background:var(--brand-red);color:var(--white);font-size:16px;font-weight:700;text-align:center;line-height:28px}
  .facts-row{left:9px;width:244px;height:26px;border-bottom:1px solid var(--rule);font-size:15.5px;line-height:26px}
  .facts-row span{position:static}
  .facts-row b{position:absolute;right:0;top:0;font-weight:800}

  .activity{left:317px;top:270px;width:264px;font-size:14.5px;line-height:18.5px;font-style:italic;color:var(--ink)}
  .activity p{position:static;margin-bottom:7px}

  .family-photo{left:604px;top:168px;width:476px;height:330px;background:var(--white);transform:rotate(4deg);box-shadow:0 4px 12px rgba(0,0,0,.35);padding:9px}
  .family-photo .scene{left:9px;top:9px;right:9px;bottom:9px;background:linear-gradient(180deg,var(--photo-sky) 0%,#c8c1b2 45%,var(--photo-lawn) 100%)}

  .quote-band{left:0;top:457px;width:1080px;height:70px;background:var(--accent-orange)}
  .quote{left:40px;top:7px;font-size:22px;line-height:28px;font-weight:800;font-style:italic;color:var(--white);letter-spacing:.3px;white-space:nowrap}

  .footer{left:0;top:527px;width:1080px;height:168px;background:var(--white)}
  .group-name{left:40px;top:565px;font-size:48px;line-height:1;font-weight:400;color:var(--ink-soft);white-space:nowrap;letter-spacing:-0.5px}
  .group-sub{left:336px;top:613px;font-size:17px;line-height:1;font-weight:400;color:var(--brand-red);white-space:nowrap}
  .website{left:112px;top:647px;font-size:20px;font-weight:700;color:var(--brand-red)}
  .footer-divider{left:510px;top:547px;width:1px;height:124px;background:var(--rule)}
  .contact{left:542px;top:553px;font-size:15px;line-height:22.5px;font-weight:700;color:var(--ink-soft);font-style:normal}
  .contact p{position:static}
  .agent{right:22px;top:555px;text-align:right}
  .agent-name{position:static;display:block;font-size:22px;font-weight:800;color:var(--brand-red);letter-spacing:.3px}
  .agent-role{position:static;display:block;font-size:19px;color:var(--ink-soft)}
  .brokerage{left:895px;top:640px;font-size:11px;font-weight:700;color:var(--ink-soft);white-space:nowrap}
  .badge{left:1010px;top:624px;width:40px;height:40px;border-radius:50%;background:#e4e4e4}
</style>
</head>
<body>
  <main class="postcard">
    <div class="area-map" role="img" aria-label="Street map of the neighborhood with price markers for sold and active homes"></div>

    <h1 class="title">Harlow Bend</h1>
    <h2 class="subtitle">Market Report of single<br>family sold and active homes</h2>
    <div class="title-rule"></div>
    <div class="report-date">October Results 2015</div>

    <div class="greeting">Dear Harlow Bend Neighbor:</div>
    <div class="intro">
      <p>We expect that this information will be useful for you to learn about the Real estate market in your neighborhood.</p>
      <p>There are 28 properties “Active for Sale” on the market, with an average price of $303,589 USD and $101.06 USD per sf.<br>Average time on market for sale 63 days.</p>
    </div>

    <section class="facts">
      <div class="facts-head">Harlow Bend 2014 Facts</div>
      <div class="facts-row" style="top:38px"><span>Single Family Properties</span><b>1,677</b></div>
      <div class="facts-row" style="top:64px"><span>Median Square Feet</span><b>2,568</b></div>
      <div class="facts-row" style="top:90px"><span>Median Lot Square Feet</span><b>7,689</b></div>
      <div class="facts-row" style="top:116px;border-bottom:none"><span>Median Year Built</span><b>2007</b></div>
    </section>

    <div class="activity">
      <p>In process, “Pending to Close” are 9 houses at average price of $252,808 USD with a sale price of $103.11 per sf.  with 34 Days on market.</p>
      <p>The past 6 Months  market behavior was as follows: 97 Houses sold at average price of $263,545 with a sale price / sqf. of $100.50</p>
    </div>

    <div class="footer"></div>

    <figure class="family-photo">
      <div class="scene" role="img" aria-label="Photo of a young family sitting on a lawn in front of a house with a sold sign"></div>
    </figure>

    <div class="quote-band">
      <p class="quote">“We will be glad to meet with you and have the<br>opportunity to help you with your Real Estate requirements”</p>
    </div>

    <div class="group-name">The Marlowe Group</div>
    <div class="group-sub">Real Estate</div>
    <div class="website">www.TheMarloweGroup.com</div>
    <div class="footer-divider"></div>
    <address class="contact">
      <p>2250 Cedar Ridge Drive</p>
      <p>Pine Hollow TX 77410</p>
      <p>C : 555 204 7731</p>
      <p>O : 555 318 6042</p>
      <p>E : renata@renatamarlowe.com</p>
    </address>
    <div class="agent">
      <span class="agent-name">RENATA MARLOWE</span>
      <span class="agent-role">Realtor</span>
    </div>
    <div class="brokerage">Northgate Realty</div>
    <div class="badge" role="img" aria-label="Partner certification badge"></div>
  </main>
</body>
</html>
```